Flaschenetikett Fenno`s ColaMix
Zielgruppe
Wir machen einen ColaMix, weil wir es können und ihm eine Prise 80er verpassen wollen.
Hip, Trendig und ein bisschen Oldschool.
Bei uns kommt nur in die Flasche, was uns selber schmeckt und dabei preislich fair ist! Kein Schnickschnack, dafür mit viel Geschmack und einer Portion Oldschool.
Einfach einen richtig guten Brausa ähhmm, ColaMix!
Farben:
orange / weiss (Hintergrund Orange & Schrift Weiss)
oder
weiss / anthrazit
Flaschenfarbe:
braun
Etikettgröße:
max. 10 x 10 cm
Name:
Fennos ColaMix
Zusatztext:
MÜNCHEN
ColaMix (muss irgendwo auf dem Etikett stehen)
Die Beispiele finden wir ultra hip, ein bisschen oldschool, trendig und genau richtig. Alles simpel, kein BlimBlim aber dafür einen ziemlich hohen Stylfaktor.
Wir sind nicht modern, sondern Kinder der 80iger, stehen auf Industrie Vintage Zeug und brauchen einen "ColaMix" der zu uns passt.
Fenno, ja einfach Fenno soll er heissen. Ein deutscher Trendname aus dem 19.Jahrhundert und doch jung und frisch! Genau wie unser ColaMix.
Das Kultgetränk das Allen schmeckt kommt in einer Oldschool braunen Flasche um die Ecke.
WIR MACHEN UNS FAST IN DIE HOSEN VOR AUFREGUNG, WAS IHR SO AUF DER FLASCHE HABT!!!!
HAUT REIN!!!

```html
<!DOCTYPE html>
<html lang="de">
<head>
<meta charset="utf-8">
<title>Fenno's ColaMix – Flaschenetikett</title>
<link rel="stylesheet" href="https://fonts.googleapis.com/css2?family=Open+Sans:wght@600&family=Libre+Baskerville:wght@700&display=swap">
<style>
  :root {
    --stage: #ececec;
    --label: #ffffff;
    --orange: #ef7f3d;
    --label-shadow: rgba(0, 0, 0, 0.28);
  }
  * { margin: 0; padding: 0; box-sizing: border-box; }
  html, body {
    width: 1200px;
    height: 857px;
    overflow: hidden;
    background: var(--stage);
  }
  .canvas {
    width: 1200px;
    height: 857px;
    display: flex;
    align-items: center;
    justify-content: center;
  }
  .label {
    position: relative;
    width: 780px;
    height: 780px;
    background: var(--label);
    box-shadow: 0 2px 8px var(--label-shadow);
    color: var(--orange);
    font-family: "Open Sans", sans-serif;
    font-weight: 600;
  }
  .brand-name {
    position: absolute;
    left: 0;
    right: 0;
    top: 120px;
    text-align: center;
    line-height: 1;
  }
  .brand-name__first {
    display: block;
    font-size: 190px;
    letter-spacing: -2px;
  }
  .brand-name__second {
    display: block;
    margin-top: 20px;
    font-size: 128px;
    letter-spacing: 2px;
  }
  .edition {
    position: absolute;
    right: 72px;
    top: 530px;
    font-family: "Libre Baskerville", serif;
    font-weight: 700;
    font-size: 19px;
    letter-spacing: 1px;
  }
  .origin {
    position: absolute;
    left: 0;
    right: 0;
    bottom: 14px;
    text-align: center;
    font-size: 36px;
  }
</style>
</head>
<body>
  <main class="canvas">
    <section class="label" aria-label="Flaschenetikett Fenno's ColaMix">
      <h1 class="brand-name">
        <span class="brand-name__first">Fenno's</span>
        <span class="brand-name__second">Cola Mix</span>
      </h1>
      <p class="edition">ORIGINAL</p>
      <p class="origin">Made for MUNICH</p>
    </section>
  </main>
</body>
</html>
```